依頼詳細
・色は1~2色
・慶事で使用できるような華やかなデザインを希望します
・弊社ロゴ画像を添付しております。どれを使用していただいても構いません。(ロゴ使用に関しては必須ではございません)
記載項目
サイズ…約200㎜(縦)×約120㎜(横)×約30㎜(高さ)
(開き方は画像をご参照頂ければと思います。)
希望イメージ
シンプル 複雑
単色 カラフル
暗い 明るい
日常 高級
遊び心 厳粛
未来的 伝統的
女性的 男性的
希望する色
納品ファイル
• イラストレーター形式 (.ai)
補足説明
向きは縦長でお願い致します。
■ 選んだ理由

華やかすぎない、上品なデザインをご提案頂いた点。
今まで弊社に無かったスタイルでありながら、弊社の他の商品ラインナップと比較した時に違和感なくラインナップに入るデザインであった点が良かったです。

■ 提案者全員のお礼・コメント

たくさんのご提案を頂き、本当にありがとうございます。
私どもでは思いもよらなかった素敵なデザインばかりで、大変感激しております。

ありがとうございました。

```html
<!DOCTYPE html>
<html lang="ja">
<head>
<meta charset="utf-8">
<title>HARUNO BAI — Gift Box Dieline</title>
<link href="https://fonts.googleapis.com/css2?family=Jost:wght@300;400&family=Noto+Serif+JP:wght@400;900&display=swap" rel="stylesheet">
<style>
  :root {
    --plum-red: #b3161f;
    --plum-red-deep: #96111a;
    --plum-red-soft: #c8323b;
    --plum-pink: #f3d4d6;
    --paper: #ffffff;
    --rule-grey: #9a9a9a;
    --label-grey: #8a8a8a;
    --ink: #111111;
  }
  html, body {
    margin: 0;
    padding: 0;
    width: 1200px;
    height: 1044px;
    overflow: hidden;
    background: var(--paper);
  }
  .dieline {
    display: block;
    width: 1200px;
    height: 1044px;
  }
  .panel-white { fill: var(--paper); }
  .cut-line { fill: none; stroke: var(--rule-grey); stroke-width: 1; }
  .lid-face { fill: var(--paper); stroke: var(--rule-grey); stroke-width: 1; }
  .side-wall { fill: url(#motif-side); }
  .flap-top { fill: url(#motif-flap-top); }
  .flap-bottom { fill: url(#motif-flap-bottom); }
  .pattern-field { fill: url(#hex-field); }
  .ribbon { fill: var(--plum-red); }
  .emblem-dot { fill: var(--plum-red); }
  .flap-blossom { fill: var(--paper); }
  .front-blossom { fill: var(--plum-red); }
  .seal { fill: var(--plum-red); }
  .brand-latin {
    font-family: "Jost", sans-serif;
    font-weight: 300;
    font-size: 13px;
    letter-spacing: 2.5px;
  }
  .brand-latin--grey { fill: var(--label-grey); }
  .brand-latin--white { fill: var(--paper); }
  .brand-kanji {
    font-family: "Noto Serif JP", serif;
    font-weight: 900;
    font-size: 46px;
    fill: var(--ink);
    writing-mode: vertical-rl;
    letter-spacing: 4px;
  }
  .origin-label {
    font-family: "Noto Serif JP", serif;
    font-weight: 400;
    font-size: 10px;
    fill: var(--ink);
    writing-mode: vertical-rl;
    letter-spacing: 1.5px;
  }
  .reading {
    font-family: "Noto Serif JP", serif;
    font-weight: 400;
    font-size: 6px;
    fill: #444444;
    writing-mode: vertical-rl;
    letter-spacing: 0.5px;
  }
</style>
</head>
<body>
<svg class="dieline" viewBox="0 0 1000 870" xmlns="http://www.w3.org/2000/svg">
  <defs>
    <radialGradient id="motif-side" cx="50%" cy="40%" r="75%">
      <stop offset="0%" stop-color="var(--plum-red-soft)"/>
      <stop offset="55%" stop-color="var(--plum-red)"/>
      <stop offset="100%" stop-color="var(--plum-red-deep)"/>
    </radialGradient>
    <linearGradient id="motif-flap-top" x1="0" y1="0" x2="1" y2="1">
      <stop offset="0%" stop-color="var(--plum-red-deep)"/>
      <stop offset="50%" stop-color="var(--plum-red)"/>
      <stop offset="100%" stop-color="var(--plum-red-soft)"/>
    </linearGradient>
    <linearGradient id="motif-flap-bottom" x1="0" y1="0" x2="1" y2="1">
      <stop offset="0%" stop-color="var(--plum-red-soft)"/>
      <stop offset="50%" stop-color="var(--plum-red)"/>
      <stop offset="100%" stop-color="var(--plum-red-deep)"/>
    </linearGradient>
    <linearGradient id="hex-field" x1="0" y1="0" x2="1" y2="1">
      <stop offset="0%" stop-color="#e9a9ad"/>
      <stop offset="50%" stop-color="var(--plum-pink)"/>
      <stop offset="100%" stop-color="#e49ba0"/>
    </linearGradient>
  </defs>

  <g class="lid">
    <path class="lid-face" d="M437 143 H60 Q44 143 44 159 V711 Q44 727 60 727 H437"/>
    <line class="cut-line" x1="88" y1="143" x2="88" y2="727"/>

    <g class="ribbon-band">
      <rect class="ribbon" x="88" y="416" width="119" height="5"/>
      <rect class="ribbon" x="88" y="424" width="119" height="5"/>
      <rect class="ribbon" x="88" y="432" width="119" height="5"/>
      <rect class="ribbon" x="340" y="416" width="97" height="5"/>
      <rect class="ribbon" x="340" y="424" width="97" height="5"/>
      <rect class="ribbon" x="340" y="432" width="97" height="5"/>
    </g>

    <circle class="emblem-dot" cx="261" cy="425" r="53"/>
    <text class="brand-latin brand-latin--grey" x="261" y="497" text-anchor="middle">HARUNO BAI</text>
  </g>

  <g class="side side--left">
    <rect class="side-wall" x="437" y="143" width="90" height="584" role="img" aria-label="Red side wall with large faint deep-red plum blossom and wave motifs"/>
    <circle class="flap-blossom" cx="480" cy="425" r="18" role="img" aria-label="White plum blossom ornament"/>
  </g>

  <g class="front">
    <rect class="flap-top" x="527" y="52" width="347" height="91" role="img" aria-label="Red flap with faint deep-red plum blossom motifs"/>
    <text class="brand-latin brand-latin--white" x="700" y="100" text-anchor="middle" transform="rotate(180 700 96)">HARUNO BAI</text>

    <rect class="panel-white" x="527" y="143" width="347" height="584"/>
    <rect class="pattern-field" x="537" y="152" width="328" height="240" role="img" aria-label="Red and white hexagonal tortoiseshell lattice with a plum blossom in each cell"/>

    <circle class="front-blossom" cx="693" cy="471" r="37" role="img" aria-label="Red plum blossom ornament"/>

    <text class="origin-label" x="738" y="528">紀州南高梅</text>
    <circle class="seal" cx="737" cy="601" r="8"/>
    <text class="brand-kanji" x="692" y="530">春野梅</text>
    <text class="reading" x="666" y="590">はるのばい</text>

    <rect class="flap-bottom" x="527" y="727" width="347" height="88" role="img" aria-label="Red flap with faint deep-red plum blossom motifs"/>
    <text class="brand-latin brand-latin--white" x="700" y="780" text-anchor="middle">HARUNO BAI</text>
  </g>

  <g class="side side--right">
    <rect class="side-wall" x="874" y="143" width="91" height="584" role="img" aria-label="Red side wall with large faint deep-red plum blossom motifs"/>
    <circle class="flap-blossom" cx="920" cy="425" r="18" role="img" aria-label="White plum blossom ornament"/>
  </g>
</svg>
</body>
</html>
```